Collectibles expert needs a new business card design.

My current business card makes me look to high end. It may even make me look arrogant or too stuffy. I do work with high end clients and their items but most of my business is with average people with average items. My business name is Walter Brumby's Old Mill Digging Co. The idea was that I mine the streets helping people discover the treasures buried in their homes. That could be art, jewelry, coins, etc. The name and an older logo I used does not make immediate sense to most people. I tried to go with just my picture and name and that is the current card I am changing. I help people who need to downsize. Whether they are getting rid of one item, a collection or a house full of items I help them discover what they have, what it is worth and what are the best ways we can get the most for them. This may be a combination of estate sale (which I dont do) auction or sell directly to a dealer or collector. Usually it is a combination of these. My main goal is to help make sure they dont accidently sell a Vandermeer painting in a garage sale. I am uploading a copy of my old card and the old logo I used to use but the winning card design will need to be much different than these. You can learn a little more about me at www.walterkbrumby.example, www.oldmilldigng.example and www.facebook.com/omdco. I hope someone can look at what I do and come up with a very unique design that will be equally effective if my client is high income or if my client is low to mid income. I do not care if it is a one or two sided card as long as it conveys my contact information and a good representation of what I do.

Target Market(s)

People who are getting rid of items. These can be elderly couples or individuals that are moving to an active living community and will have less space so they need to sell items. This can also include the children of elder parents that dont want their stuff and want to find solutions to help them get rid of their items.

Contact Information for Business Card

The card should have my business name Walter Brumby's Old Mill Digging Co., phone number 555-312-70981, email walter@oldmilldigging.example and website www.oldmilldigging.example. Would also like to include Buyer, Broker, Consultant and Appraiser. We can put Walter K. Brumby, ISA on the opposite side of the company name since it includes my name as well.

Font styles to use
Sans Serif

Colors

Designer to choose colors to be used in the design.

Requirements
Must have
• My project must have a professional look. It must not alienate low income clients and should still be appealing to high value clients.

```html
<!DOCTYPE html>
<html lang="en">
<head>
<meta charset="utf-8">
<title>Walter Brumby's Old Mill Digging Co. — Business Card</title>
<link href="https://fonts.googleapis.com/css2?family=Oswald:wght@300;400;500&display=swap" rel="stylesheet">
<style>
  :root {
    --backdrop: #9ea9ad;
    --card-dark: #3a3129;
    --card-deeper: #241d18;
    --gold: #a97b2e;
    --taupe: #b7a78b;
    --paper: #ffffff;
    --cream: #ece4d8;
    --badge-teal: #2f5c6c;
    --photo-tone: #6b5a4c;
  }
  html, body {
    margin: 0;
    padding: 0;
    width: 1200px;
    height: 2400px;
    overflow: hidden;
    background: var(--backdrop);
    font-family: "Oswald", "Arial Narrow", sans-serif;
  }
  .canvas { position: relative; width: 1200px; height: 2400px; }
  .card {
    position: absolute;
    left: 45px;
    width: 1111px;
    height: 612px;
    border-radius: 14px;
    overflow: hidden;
    background: var(--card-dark);
    box-shadow: 0 6px 18px rgba(0,0,0,0.25);
  }
  .card--company { top: 528px; }
  .card--person { top: 1260px; }
  .card-shapes { position: absolute; inset: 0; }

  .owner-line {
    position: absolute; left: 55px; top: 84px; margin: 0;
    color: var(--gold); font-weight: 500; font-size: 31px;
    letter-spacing: 0.5px; line-height: 1;
  }
  .company-line {
    position: absolute; left: 55px; top: 126px; margin: 0;
    color: var(--cream); font-weight: 300; font-size: 31px;
    letter-spacing: 0.5px; line-height: 1;
  }
  .services {
    position: absolute; left: 55px; top: 196px; margin: 0;
    color: var(--cream); font-weight: 300; font-size: 24px; line-height: 1;
  }
  .contact {
    position: absolute; left: 125px; margin: 0;
    color: var(--cream); font-weight: 300; font-size: 24px; line-height: 1;
  }
  .contact--phone { top: 418px; }
  .contact--email { top: 476px; }
  .website {
    position: absolute; left: 758px; top: 543px; margin: 0;
    color: var(--paper); font-weight: 400; font-size: 22px; line-height: 1;
  }
  .mascot-art {
    position: absolute; left: 696px; top: 149px;
    width: 312px; height: 312px; border-radius: 50%;
    background: radial-gradient(circle at 50% 45%, #3c6e80, var(--badge-teal));
  }
  .portrait {
    position: absolute; left: 89px; top: 113px;
    width: 374px; height: 374px; border-radius: 50%;
    background: linear-gradient(160deg, #8a7462, var(--photo-tone) 55%, #2e2a28);
    box-shadow: 0 0 0 4px var(--card-dark), 0 0 0 8px var(--gold);
  }
  .person-name {
    position: absolute; left: 516px; top: 246px; margin: 0;
    color: var(--paper); font-weight: 500; font-size: 50px;
    letter-spacing: 1px; line-height: 1;
  }
  .credential {
    position: absolute; left: 571px; top: 338px; margin: 0;
    color: var(--cream); font-weight: 400; font-size: 20px;
    letter-spacing: 18px; line-height: 1;
  }
</style>
</head>
<body>
<main class="canvas">

  <section class="card card--company" aria-label="Card front with company details">
    <svg class="card-shapes" width="1111" height="612" viewBox="0 0 1111 612" aria-hidden="true">
      <polygon points="595,0 1111,0 1111,612 696,612" fill="var(--paper)"/>
      <polygon points="456,0 595,0 623,168" fill="var(--gold)"/>
      <rect x="55" y="176" width="533" height="2" fill="var(--gold)"/>
      <rect x="0" y="418" width="108" height="28" fill="var(--gold)"/>
      <rect x="0" y="476" width="108" height="28" fill="var(--gold)"/>
      <!-- phone icon -->
      <path d="M82 424 c-3 0 -6 3 -5 7 c2 6 7 11 13 13 c4 1 7 -2 7 -5 l-4 -3 l-3 2 c-3 -1 -6 -4 -7 -7 l2 -3 z" fill="var(--paper)"/>
      <!-- mail icon -->
      <rect x="76" y="482" width="22" height="16" rx="1" fill="var(--paper)"/>
      <path d="M76 483 l11 8 l11 -8" fill="none" stroke="var(--gold)" stroke-width="2"/>
      <rect x="0" y="545" width="240" height="26" fill="var(--card-deeper)"/>
      <polygon points="252,545 372,545 364,571 252,571" fill="var(--taupe)"/>
      <polygon points="384,545 1111,545 1111,571 376,571" fill="var(--gold)"/>
      <!-- globe icon -->
      <circle cx="740" cy="558" r="9" fill="none" stroke="var(--paper)" stroke-width="2"/>
      <ellipse cx="740" cy="558" rx="4" ry="9" fill="none" stroke="var(--paper)" stroke-width="1.5"/>
      <line x1="731" y1="558" x2="749" y2="558" stroke="var(--paper)" stroke-width="1.5"/>
    </svg>
    <p class="owner-line">WALTER BRUMBY'S</p>
    <p class="company-line">OLD MILL DIGGING CO</p>
    <p class="services">Buyer, Broker, Consultant and Appraiser</p>
    <p class="contact contact--phone">555-312-70981,</p>
    <p class="contact contact--email">walter@oldmilldigging.example</p>
    <div class="mascot-art" role="img" aria-label="Illustration of a vintage miner woman with a pickaxe seated on an ore cart"></div>
    <p class="website">www.oldmilldigging.example</p>
  </section>

  <section class="card card--person" aria-label="Card back with personal name">
    <svg class="card-shapes" width="1111" height="612" viewBox="0 0 1111 612" aria-hidden="true">
      <rect x="516" y="328" width="595" height="3" fill="var(--gold)"/>
      <polygon points="522,336 1111,336 1111,365 516,365" fill="var(--gold)"/>
    </svg>
    <div class="portrait" role="img" aria-label="Portrait photograph of Walter K. Brumby"></div>
    <h1 class="person-name">WALTER K. BRUMBY</h1>
    <p class="credential">ISA</p>
  </section>

</main>
</body>
</html>
```